Rebrand of 3 bottle labels for nail polish brand

The task is to make a rebranding of our current gel nail polish bottle design. We have become one of the leading european nail polish brand, so we want to improve the quality of the label design to a more scandinavian and minimalistic bottle design, which stille has to be recognisable and unique.

We have attached a more detailed description of the rebranding instructions for our gel polish bottles called "bottle task".
Updates

The Labels should not be just Black and White as stated. But should be mainly Black and White and then some of our color as explained in the uploaded file.

Target Market(s)

Girls and women age 18-55 Northern Europe

Industry/Entity Type

Cosmetic/ Nail Gel Polish

Colors

Designer to choose only greyscale colors for use in the design.

Requirements
Must have
• See attched design instruction
Nice to have
• Moderne, Minimalist, Recognizable and Unique look
Should not have
• Too many elements, too busy design

```html
<!DOCTYPE html>
<html lang="en">
<head>
<meta charset="utf-8">
<title>Lumelle Color Coat Labels</title>
<link href="https://fonts.googleapis.com/css2?family=Montserrat:wght@300;400;500;600;700&display=swap" rel="stylesheet">
<style>
:root{
  --page:#ffffff;
  --label:#000000;
  --ink:#ffffff;
  --yellow:#efcf33;
  --rose:#a5605a;
  --snow:#e6e6e6;
  --dark-ink:#111111;
}
*{box-sizing:border-box;margin:0;padding:0}
html,body{width:1200px;height:1200px;overflow:hidden;background:var(--page)}
body{position:relative;font-family:"Montserrat",sans-serif;color:var(--ink)}
.label{position:absolute;left:104px;width:994px;height:265px;background:var(--label)}
.label--yellow{top:98px;--shade:var(--yellow);--shade-ink:var(--dark-ink)}
.label--rose{top:467px;--shade:var(--rose);--shade-ink:var(--ink)}
.label--snow{top:836px;--shade:var(--snow);--shade-ink:var(--dark-ink)}

.front{position:absolute;left:132px;top:0;width:200px;text-align:center}
.brand{position:absolute;left:-28px;top:12px;width:256px;font-size:70px;font-weight:400;letter-spacing:1px;line-height:1}
.tm{position:absolute;left:242px;top:17px;font-size:10px;font-weight:600}
.product{position:absolute;left:0;top:92px;width:200px;font-size:17px;font-weight:500;letter-spacing:1.5px}
.system{position:absolute;left:0;top:112px;width:200px;font-size:9.5px;font-weight:300;letter-spacing:.5px}
.shade-number{position:absolute;left:78px;top:135px;width:44px;height:44px;border:3px solid var(--shade);border-radius:4px;font-size:23px;font-weight:500;line-height:38px}
.shade-band{position:absolute;left:8px;top:195px;width:186px;height:34px;background:var(--shade);color:var(--shade-ink);font-size:16.5px;font-weight:500;letter-spacing:.5px;line-height:34px}
.claim{position:absolute;left:0;top:234px;width:200px;font-size:14px;font-weight:400;letter-spacing:.4px}

.info{position:absolute;left:532px;top:28px;width:282px;font-size:9px;font-weight:300;line-height:11.2px}
.info p{margin-bottom:11.5px}
.info p:nth-child(4){margin-bottom:16px}
.info strong{font-weight:700}

.volume{position:absolute;left:857px;top:101px;width:16px;height:62px;border:1.2px solid var(--ink);border-radius:8px}
.volume span{position:absolute;left:50%;top:50%;transform:translate(-50%,-50%) rotate(-90deg);white-space:nowrap;font-size:7px;font-weight:300}
.icons{position:absolute;left:894px;top:102px}
.origin{position:absolute;left:923px;top:154px;transform:translate(-50%,-50%) rotate(-90deg);white-space:nowrap;font-size:10.5px;font-weight:400}
.address{position:absolute;left:937px;top:128px;transform:translate(-50%,-50%) rotate(-90deg);white-space:nowrap;font-size:5.6px;font-weight:300}
</style>
</head>
<body>

<section class="label label--yellow">
  <div class="front">
    <div class="brand">lumelle</div><span class="tm">TM</span>
    <div class="product">COLOR COAT</div>
    <div class="system">SOAK OFF UV/LED</div>
    <div class="shade-number">21</div>
    <div class="shade-band">YELLOW</div>
    <div class="claim">Vegan Formula</div>
  </div>
  <div class="info">
    <p><strong>DIRECTIONS FOR USE (ENG):</strong> Lumelle Color Coat must be applied in thin layers and cured in one of our Lumelle Lamps.</p>
    <p><strong>ANVENDELSE (DK):</strong> Lumelle Farver skal påføres i tynde lag og hærdes i en af vores Lumelle Lamper.</p>
    <p><strong>CAUTION (ENG):</strong> Keep out of reach of children. Discontinue use if irritation occurs. Avoid direct sunlight or extreme exposure to LED or UV Light.</p>
    <p><strong>ADVARSEL (DK):</strong> Opbevar utilgængelit for børn. Stop din behandling, hvis produktet forudsager irritation. undgå direkte sollys eller udsættelse for LED eller UV.</p>
    <p><strong>INGREDIENTS:</strong> Acrylates Copolymer, Acrylated Aliphatic Urethane, Cellulose Acetate Butanoate, Dimethicone, Cresine, Wax, Pigment Red, Carbon Black, Titanium dioxide, CI 77891</p>
  </div>
  <div class="volume"><span>15ml e 0.5oz</span></div>
  <svg class="icons" width="20" height="62" viewBox="0 0 20 62" fill="none" stroke="#fff" stroke-width="1.4">
    <rect x="3" y="4" width="5" height="7" fill="#fff" stroke="none"/><rect x="10" y="1" width="6" height="10" fill="#fff" stroke="none"/>
    <circle cx="10" cy="22" r="5.5" stroke-width="2.5"/>
    <path d="M3 37 L8 47 M8 37 L8 47 M11 36 h6 v11 h-6z"/>
    <path d="M10 52 L15 57 L10 62 L5 57 Z"/>
  </svg>
  <div class="origin">Made in Germany</div>
  <div class="address">Nordic Labs ApS - Havnevej 14B 2450 Sydhavn, Denmark</div>
</section>

<section class="label label--rose">
  <div class="front">
    <div class="brand">lumelle</div><span class="tm">TM</span>
    <div class="product">COLOR COAT</div>
    <div class="system">SOAK OFF UV/LED</div>
    <div class="shade-number">21</div>
    <div class="shade-band">ROSE GOLD</div>
    <div class="claim">Vegan Formula</div>
  </div>
  <div class="info">
    <p><strong>DIRECTIONS FOR USE (ENG):</strong> Lumelle Color Coat must be applied in thin layers and cured in one of our Lumelle Lamps.</p>
    <p><strong>ANVENDELSE (DK):</strong> Lumelle Farver skal påføres i tynde lag og hærdes i en af vores Lumelle Lamper.</p>
    <p><strong>CAUTION (ENG):</strong> Keep out of reach of children. Discontinue use if irritation occurs. Avoid direct sunlight or extreme exposure to LED or UV Light.</p>
    <p><strong>ADVARSEL (DK):</strong> Opbevar utilgængelit for børn. Stop din behandling, hvis produktet forudsager irritation. undgå direkte sollys eller udsættelse for LED eller UV.</p>
    <p><strong>INGREDIENTS:</strong> Acrylates Copolymer, Acrylated Aliphatic Urethane, Cellulose Acetate Butanoate, Dimethicone, Cresine, Wax, Pigment Red, Carbon Black, Titanium dioxide, CI 77891</p>
  </div>
  <div class="volume"><span>15ml e 0.5oz</span></div>
  <svg class="icons" width="20" height="62" viewBox="0 0 20 62" fill="none" stroke="#fff" stroke-width="1.4">
    <rect x="3" y="4" width="5" height="7" fill="#fff" stroke="none"/><rect x="10" y="1" width="6" height="10" fill="#fff" stroke="none"/>
    <circle cx="10" cy="22" r="5.5" stroke-width="2.5"/>
    <path d="M3 37 L8 47 M8 37 L8 47 M11 36 h6 v11 h-6z"/>
    <path d="M10 52 L15 57 L10 62 L5 57 Z"/>
  </svg>
  <div class="origin">Made in Germany</div>
  <div class="address">Nordic Labs ApS - Havnevej 14B 2450 Sydhavn, Denmark</div>
</section>

<section class="label label--snow">
  <div class="front">
    <div class="brand">lumelle</div><span class="tm">TM</span>
    <div class="product">COLOR COAT</div>
    <div class="system">SOAK OFF UV/LED</div>
    <div class="shade-number">21</div>
    <div class="shade-band">SNOW</div>
    <div class="claim">Vegan Formula</div>
  </div>
  <div class="info">
    <p><strong>DIRECTIONS FOR USE (ENG):</strong> Lumelle Color Coat must be applied in thin layers and cured in one of our Lumelle Lamps.</p>
    <p><strong>ANVENDELSE (DK):</strong> Lumelle Farver skal påføres i tynde lag og hærdes i en af vores Lumelle Lamper.</p>
    <p><strong>CAUTION (ENG):</strong> Keep out of reach of children. Discontinue use if irritation occurs. Avoid direct sunlight or extreme exposure to LED or UV Light.</p>
    <p><strong>ADVARSEL (DK):</strong> Opbevar utilgængelit for børn. Stop din behandling, hvis produktet forudsager irritation. undgå direkte sollys eller udsættelse for LED eller UV.</p>
    <p><strong>INGREDIENTS:</strong> Acrylates Copolymer, Acrylated Aliphatic Urethane, Cellulose Acetate Butanoate, Dimethicone, Cresine, Wax, Pigment Red, Carbon Black, Titanium dioxide, CI 77891</p>
  </div>
  <div class="volume"><span>15ml e 0.5oz</span></div>
  <svg class="icons" width="20" height="62" viewBox="0 0 20 62" fill="none" stroke="#fff" stroke-width="1.4">
    <rect x="3" y="4" width="5" height="7" fill="#fff" stroke="none"/><rect x="10" y="1" width="6" height="10" fill="#fff" stroke="none"/>
    <circle cx="10" cy="22" r="5.5" stroke-width="2.5"/>
    <path d="M3 37 L8 47 M8 37 L8 47 M11 36 h6 v11 h-6z"/>
    <path d="M10 52 L15 57 L10 62 L5 57 Z"/>
  </svg>
  <div class="origin">Made in Germany</div>
  <div class="address">Nordic Labs ApS - Havnevej 14B 2450 Sydhavn, Denmark</div>
</section>

</body>
</html>
```